Crestline Delivery Partners Business Card Redesign Project

CRESTLINE DELIVERY PARTNERS
Our company needs to have its business cards redesigned as the current design no longer reflects the business brand or attracts the type of clientele we are seeking.

MUST LOOK
★ Upmarket
★ Reflect Quality
★ Corporate feel
★ Professional
★ Innovative
★ Colourful

MUST PROMOTE
★ Market Leader
★ Knowledge
★ Expertise
★ Experience
★ Solutions
★ Advice

MUST FEEL
★ Classy
★ Elegant
★ Savvy
★ Edgy
★ Upbeat

WHAT WE DO
Crestline Delivery Partners provides project management and project controls consultancy services to companies in many industry sectors, within Australia and overseas. My company has developed a business brand through forging strong business relationships within industry. We provide innovative tools, concepts and solutions to management teams to assist them in better plan and managing there project portfolios.

SECTORS OF INDUSTRY WE SERVICE
★Oil & Gas
★Minerals & Metals
★Petrochemical
★Manufacturing
★Building & Construction
★Telecommunications
★Rail
★Civil

BUSINESS CARD DETAILS REQUIRED ON FRONT
Marcus Feldwick
Business Owner
Tel: 0498357162
Email: marcusfeldwick@crestlinedeliverypartners.com
Website: www.crestlinedeliverypartners.com.au

BUSINESS CARD DETAILS REQUIRED ON BACK
Providing | Knowledge | Expertise | Experience

ATTACHMENTS
Business Logo

Target Market(s)

Oil & Gas I Mining & Resources I Industry in General
Upmarket Clientele
Corporate World

Industry/Entity Type

Industry

Requirements
Must have
• Must be creative and a unique design
The business card must have information on the front and back

```html
<!DOCTYPE html>
<html lang="en">
<head>
<meta charset="utf-8">
<title>Crestline Delivery Partners – Card Back</title>
<link rel="stylesheet" href="https://fonts.googleapis.com/css2?family=Arimo:wght@400;700&display=swap">
<style>
  :root {
    --grey-dark: #6f6f71;
    --grey-mid: #b9b9bb;
    --grey-light: #ececec;
    --brand-red: #b30a12;
    --accent-red: #e8202a;
    --streak-red: #e65a5e;
    --ink: #1e1e1e;
    --white: #ffffff;
    --divider: #9a9a9a;
  }
  * { margin: 0; padding: 0; box-sizing: border-box; }
  html, body { width: 1200px; height: 676px; overflow: hidden; background: var(--white); }
  .card {
    position: relative;
    width: 1200px;
    height: 676px;
    overflow: hidden;
    font-family: "Arimo", Arial, sans-serif;
    background: linear-gradient(180deg, var(--grey-dark) 0%, var(--grey-mid) 22%, var(--grey-light) 55%, #f4f4f4 70%);
  }
  .card__waves { position: absolute; inset: 0; width: 1200px; height: 676px; }
  .motto {
    position: absolute; top: 32px; left: 0; width: 100%;
    text-align: center; color: var(--white);
    font-weight: 700; font-size: 35px; letter-spacing: 0.5px;
  }
  .about {
    position: absolute; top: 100px; left: 49px; width: 1110px;
    color: var(--ink); font-size: 22.4px; line-height: 38px;
  }
  .sectors {
    position: absolute; top: 313px; left: 0; width: 100%; text-align: center;
  }
  .sectors__title {
    color: var(--accent-red); font-weight: 700; font-size: 37px; letter-spacing: 0.3px;
    margin-left: 30px;
  }
  .sectors__row {
    color: var(--ink); font-size: 24px; line-height: 39px; margin-top: 2px;
  }
  .sectors__row + .sectors__row { margin-top: 0; }
  .sectors__row span + span::before {
    content: ""; display: inline-block; width: 1px; height: 24px;
    background: var(--divider); margin: 0 12px -3px;
  }
  .brand {
    position: absolute; left: 648px; top: 548px;
    display: flex; align-items: center; gap: 14px;
  }
  .brand__mark { width: 44px; height: 44px; background: var(--ink); }
  .brand__name {
    color: var(--ink); font-weight: 700; font-size: 25px; letter-spacing: 0.3px;
  }
  .brand__tagline {
    position: absolute; left: 706px; top: 592px;
    color: var(--ink); font-weight: 700; font-size: 11.5px;
  }
</style>
</head>
<body>
<div class="card">
  <svg class="card__waves" viewBox="0 0 1028 579" preserveAspectRatio="none" aria-hidden="true">
    <path d="M0,445 C120,470 260,470 420,448 C640,418 860,392 1028,392 L1028,579 L0,579 Z" fill="#ffffff"/>
    <path d="M0,460 C140,478 300,472 460,448 C660,420 860,404 1028,408 L1028,579 L0,579 Z" fill="var(--brand-red)"/>
    <path d="M0,378 C60,410 150,440 290,456 C160,452 60,440 0,425 Z" fill="var(--streak-red)"/>
    <path d="M0,425 C60,440 160,452 290,456" fill="none" stroke="#ffffff" stroke-width="2"/>
  </svg>

  <h2 class="motto">Providing | Knowledge | Expertise | Experience</h2>

  <p class="about">Crestline Delivery Partners provides project management and project controls consultancy services to companies in many industry sectors, within Australia and overseas. My company has been developing a business brand through forging strong business relationships within industry. We provide innovative tools, concepts and solutions to management teams to assist them in better plan and managing there project portfolios.</p>

  <section class="sectors">
    <h3 class="sectors__title">SECTORS OF INDUSTRY WE SERVICE</h3>
    <p class="sectors__row"><span>Oil &amp; Gas</span><span>Minerals &amp; Metals</span><span>Petrochemical</span><span>Manufacturing</span></p>
    <p class="sectors__row"><span>Building &amp; Construction</span><span>Telecommunications</span><span>Rail</span><span>Civil</span></p>
  </section>

  <div class="brand">
    <div class="brand__mark"></div>
    <div class="brand__name">CRESTLINE DELIVERY PARTNERS</div>
  </div>
  <p class="brand__tagline">Providing Effective Project Controls and Management Solutions</p>
</div>
</body>
</html>
```